Letterhead to Prospective Clients

Create a letterhead (word & canva) that I will use to send letters to prospective clients and also include the Harbourline Estate Group Logo, My Contact Details and Interchangeable "Suburb". Use the same font and colour pallete

Maris Toppel | "Suburb" Specialist - Redlands & Surrounds
Mobile: 0417 862 905
Email: MT@HarbourlineEstateGroup.com.au

```html
<!DOCTYPE html>
<html lang="en">
<head>
<meta charset="utf-8">
<title>Harbourline Estate Group Letterhead</title>
<link href="https://fonts.googleapis.com/css2?family=Poppins:wght@300;400;600&display=swap" rel="stylesheet">
<style>
  :root {
    --backdrop: #a3aaa6;
    --paper: #f2f2f1;
    --navy: #1b2c4a;
    --tan: #c9a07a;
    --grey: #8b8d90;
  }
  * { margin: 0; padding: 0; box-sizing: border-box; }
  html, body {
    width: 1200px; height: 803px; overflow: hidden;
    background: var(--backdrop);
    font-family: "Poppins", sans-serif;
  }
  .letterhead {
    position: absolute;
    left: 331px; top: 21px;
    width: 538px; height: 761px;
    background: var(--paper);
    box-shadow: 0 6px 18px rgba(0,0,0,0.18);
  }
  .brand {
    position: absolute;
    top: 52px; left: 0; right: 0;
    text-align: center;
    color: var(--navy);
    font-weight: 300;
    font-size: 17px;
    letter-spacing: 0.16em;
    text-transform: uppercase;
  }
  .contact-line {
    position: absolute;
    left: 33px; right: 24px; bottom: 26px;
    display: flex; align-items: center;
    font-size: 7.4px;
    white-space: nowrap;
    color: var(--grey);
  }
  .agent-name { color: var(--navy); font-weight: 600; }
  .divider { color: var(--navy); margin: 0 3px; }
  .agent-role { color: var(--tan); }
  .wave { margin: 0 6px 0 5px; }
  .contact-item { display: flex; align-items: center; margin-right: 6px; }
  .contact-item svg { margin-right: 3px; }
  .base-band {
    position: absolute; left: 0; right: 0; bottom: 0;
    height: 6px; display: flex;
  }
  .base-band .navy-part { width: 51%; background: var(--navy); }
  .base-band .gap { width: 2px; background: var(--paper); }
  .base-band .tan-part { flex: 1; background: var(--tan); }
</style>
</head>
<body>
  <main class="letterhead">
    <header class="brand">Harbourline Estate Group</header>

    <footer class="contact-line">
      <span class="agent-name">Maris Toppel</span>
      <span class="divider">|</span>
      <span class="agent-role">“Suburb” Specialist - Redlands &amp; Surrounds</span>
      <svg class="wave" width="12" height="5" viewBox="0 0 12 5" aria-hidden="true">
        <path d="M0.5 3.2 C2.5 0.5 4.5 0.5 6 2.5 C7.5 4.5 9.5 4.5 11.5 1.8" fill="none" stroke="var(--tan)" stroke-width="0.9"/>
      </svg>
      <span class="contact-item">
        <svg width="5" height="8" viewBox="0 0 5 8" aria-hidden="true">
          <rect x="0.5" y="0.5" width="4" height="7" rx="0.8" fill="none" stroke="var(--tan)" stroke-width="0.8"/>
        </svg>
        0417 862 905
      </span>
      <span class="contact-item">
        <svg width="7" height="5" viewBox="0 0 7 5" aria-hidden="true">
          <rect x="0" y="0" width="7" height="5" rx="0.6" fill="var(--tan)"/>
          <path d="M0.4 0.5 L3.5 2.8 L6.6 0.5" fill="none" stroke="var(--paper)" stroke-width="0.6"/>
        </svg>
        MT@HarbourlineEstateGroup.com.au
      </span>
    </footer>

    <div class="base-band">
      <div class="navy-part"></div>
      <div class="gap"></div>
      <div class="tan-part"></div>
    </div>
  </main>
</body>
</html>
```